Hydraulics Company Business Card Design

Modern business card design for a hydraulics company.
Our company colours are - black, orange and white.
I would like the following contact details included-
Name
Position
Phone number
Email
Website
Street Address

I have attached our company logo.
I would like the back of the card white.

Thank you.

```html
<!DOCTYPE html>
<html lang="en">
<head>
<meta charset="utf-8">
<title>Brindle Creek Hydraulics — Business Card</title>
<link href="https://fonts.googleapis.com/css2?family=Poppins:wght@300;400;600;800&display=swap" rel="stylesheet">
<style>
  :root {
    --stage: #0e0e0e;
    --card: #262627;
    --orange: #f7941d;
    --white: #e9e9e9;
    --rule: #4a4a4a;
  }
  * { margin: 0; padding: 0; box-sizing: border-box; }
  html, body { width: 1200px; height: 820px; overflow: hidden; background: var(--stage); }
  body { position: relative; font-family: "Poppins", sans-serif; }

  .card {
    position: absolute;
    width: 540px;
    height: 310px;
    background: var(--card);
    border-radius: 2px;
  }
  .card--front { left: 40px; top: 255px; box-shadow: 0 0 0 1.5px var(--orange); }
  .card--back  { left: 620px; top: 255px; box-shadow: 0 4px 0 var(--orange), 0 0 0 1px #3a2a12; }

  .brand {
    position: absolute;
    display: flex;
    align-items: center;
    gap: 10px;
    color: var(--orange);
    font-weight: 800;
    letter-spacing: -0.3px;
    line-height: 1;
    white-space: nowrap;
  }
  .brand__square { background: var(--orange); flex: none; }
  .card--front .brand { right: 36px; top: 58px; font-size: 24px; }
  .card--front .brand__square { width: 14px; height: 14px; }
  .card--back .brand { left: 50%; top: 50%; transform: translate(-50%, -50%); font-size: 30px; }
  .card--back .brand__square { width: 18px; height: 18px; }

  .rule { position: absolute; height: 1px; background: var(--rule); }
  .rule--long  { right: 36px; top: 150px; width: 300px; }
  .rule--short { left: 36px; top: 212px; width: 150px; }

  .person { position: absolute; left: 36px; top: 160px; }
  .person__name { color: var(--orange); font-weight: 600; font-size: 17px; letter-spacing: 0.3px; line-height: 1.2; }
  .person__role { color: var(--white); font-weight: 400; font-size: 13px; line-height: 1.3; }

  .contacts { position: absolute; left: 36px; top: 224px; list-style: none; }
  .contacts li {
    display: flex; align-items: center; gap: 8px;
    color: var(--white); font-weight: 300; font-size: 13px; line-height: 20px;
  }
  .contacts svg { width: 12px; height: 12px; flex: none; }

  .address {
    position: absolute; right: 36px; top: 166px;
    text-align: right; color: var(--white);
    font-weight: 300; font-size: 12.5px; line-height: 1.35; font-style: normal;
  }
</style>
</head>
<body>

<section class="card card--front" aria-label="Business card front">
  <div class="brand"><span class="brand__square"></span>Brindle Creek Hydraulics</div>

  <div class="rule rule--long"></div>

  <div class="person">
    <p class="person__name">MARCUS HALE</p>
    <p class="person__role">Managing Director</p>
  </div>

  <div class="rule rule--short"></div>

  <ul class="contacts">
    <li>
      <svg viewBox="0 0 24 24" aria-hidden="true"><path fill="var(--orange)" d="M6.6 10.8a15.1 15.1 0 0 0 6.6 6.6l2.2-2.2c.3-.3.7-.4 1-.2 1.1.4 2.3.6 3.6.6.6 0 1 .4 1 1V20c0 .6-.4 1-1 1A17 17 0 0 1 3 4c0-.6.4-1 1-1h3.5c.6 0 1 .4 1 1 0 1.3.2 2.5.6 3.6.1.3 0 .7-.2 1z"/></svg>
      044-555 018 274
    </li>
    <li>
      <svg viewBox="0 0 24 24" aria-hidden="true"><path fill="var(--orange)" d="M2 5h20v14H2zm2 2v.5l8 5 8-5V7l-8 5z"/></svg>
      hello@brindlecreek.com
    </li>
    <li>
      <svg viewBox="0 0 24 24" aria-hidden="true"><g fill="none" stroke="var(--orange)" stroke-width="2"><circle cx="12" cy="12" r="9"/><ellipse cx="12" cy="12" rx="4" ry="9"/><path d="M3 12h18M5 7h14M5 17h14"/></g></svg>
      www.brindlecreek.com
    </li>
  </ul>

  <address class="address">421, Address line goes here<br>45452,Country Name</address>
</section>

<section class="card card--back" aria-label="Business card back">
  <div class="brand"><span class="brand__square"></span>Brindle Creek Hydraulics</div>
</section>

</body>
</html>
```